BrightLoop (1 page) homepage re-design

Our homepage needs a face-lift! We need our homepage on our website re-designed with a fresh and current look and feel. We have all the details, colour codes and a rough wireframe ready, but need a talented designer to put some personality into our ideas.

What we do: BrightLoop is a digital marketing agency with offices in Australia (Sydney) and South Africa (Cape Town). We specialise in SEO, PPC (otherwise known as Zentro PayLine or SEM), content marketing and Zentro Tallyboard. We use these tools to help our clients realise their business dreams.

VISUAL

Style / theme of the design:
Clean, simplistic, fun, flow.

Websites we draw inspiration from:
This is the theme we want to use to build the website
http://demo.vormalayouts.example/vl/?theme=Pebbled
Inspiration:
https://www.ondrapromo.example/
https://www.nelvagrowth.example.au/
https://quimbel.example.au/
https://torvin.layout-works.example/forum/

What we like about the site:
Clean, simple design, good use of white space. The subtle changing background colours, strong contrast with text. Not too busy or distracting.

What we don’t want: Too many different colours.

Target Market(s)

Our target audience: Marketing Managers of small to medium size businesses in Australia.

Industry/Entity Type

Marketing

Number of Pages Required

1 page

Font styles to use
Sans Serif

Requirements
Must have
• Elements to be added on homepage in order and as seen in attachments:
• - Section 1: Video with team as image and a play button add the heading: We help smart marketing managers achieve their KPIs [line break] and reduce their digital marketing overwhelm.
• - Section 2: Solutions section with the 6 solutions displayed in a row.
• - Section 3: Register Free Webinar with video
• - Section 4: Please add 3 case studies (as seen in attached docs there is only 1 but please add 3 below each other)
• - Section 5: Clients. Please add all client logo’s (black and white)
• - Section 6: Our Blog (as seen attached)
• - Section 7: Conferences Attended (please add the title and a paragraph of lorem Ipsom below) and then please add all conference logo’s attached below.
• - Section 8: In The Media (please add all logo’s titled media) white background
• - Section 9: Footer (dark grey footer) add our Zentro honoured affiliate logo here please
• - Section10: Footer - include:
• - Social logos (WorkMesh, Blipster, Pallwall, ReelDrop, Zentro Hub)
• - Navigation
• - Contact details (name, address, phone number, email)
• Colour codes:
• We want to use light greys, white and charcoal grey for the backgrounds with a pop of our green colour to bring out our branding and all CTA’s to be orange, colour codes below:
• Light grey: #F2F2F2
• Charcoal grey: #161616
• Green: #428E29
• CTA’s: #de7532
• PLEASE NOTE: Please see attached pdf titled: homepagecopybrief.pdf for all the titles and statistics that need to go on the homepage
Should not have
• Too much colour, icons should not be different colours

```html
<!DOCTYPE html>
<html lang="en">
<head>
<meta charset="utf-8">
<title>BrightLoop — Digital Marketing Agency</title>
<link rel="stylesheet" href="https://fonts.googleapis.com/css2?family=Oswald:wght@300;400;500;600;700&family=Open+Sans:wght@400;600;700&display=swap">
<style>
:root{
  --green:#428E29;
  --green-dark:#2f7420;
  --orange:#de7532;
  --charcoal:#161616;
  --footer:#1d1d1d;
  --light:#F2F2F2;
  --white:#ffffff;
  --text:#333333;
  --muted:#8a8a8a;
  --link-blue:#2b7cc0;
  --head:"Oswald",sans-serif;
  --body:"Open Sans",sans-serif;
}
*{box-sizing:border-box;margin:0;padding:0}
html,body{width:1200px;height:4749px;overflow:hidden}
body{font-family:var(--body);color:var(--text);background:var(--white);position:relative}
section,header,footer{position:relative;width:1200px;overflow:hidden}
.abs{position:absolute}
.section-title{position:absolute;left:0;width:1200px;text-align:center;font-family:var(--head);font-weight:600;font-size:25px;letter-spacing:.5px;color:var(--charcoal);text-transform:uppercase}
.section-intro{position:absolute;left:380px;width:440px;text-align:center;font-size:11px;line-height:17px;color:#777}
.btn{display:inline-block;background:var(--orange);color:var(--white);font-family:var(--head);font-size:10px;font-weight:500;letter-spacing:.5px;text-transform:uppercase;padding:4px 10px;border-radius:2px}

/* hero */
.hero{height:586px}
.hero-media{position:absolute;inset:0;background:radial-gradient(circle at 62% 40%,#9a9a96 0%,#6b6d6a 35%,#3d3f3d 75%,#2a2b2a 100%)}
.hero-shade{position:absolute;inset:0;background:linear-gradient(180deg,rgba(0,0,0,.25),rgba(0,0,0,.35))}
.brand{position:absolute;left:231px;top:10px;display:flex;align-items:center;gap:6px;font-family:var(--head);font-weight:600;font-size:15px;letter-spacing:1px;color:var(--white)}
.brand-mark{width:12px;height:12px;background:var(--green)}
.main-nav{position:absolute;left:497px;top:13px;display:flex;gap:17px;font-family:var(--head);font-size:10px;letter-spacing:.4px;color:var(--white)}
.main-nav .active{color:var(--orange)}
.play{position:absolute;left:579px;top:269px}
.hero-title{position:absolute;top:348px;width:1200px;text-align:center;font-family:var(--head);font-weight:700;font-size:46px;color:var(--white);line-height:52px}
.hero-sub{position:absolute;top:407px;width:1200px;text-align:center;font-family:var(--head);font-weight:500;font-size:19px;color:var(--white)}

/* solutions */
.solutions{height:668px}
.solution{position:absolute;width:200px}
.solution svg{display:block;margin:0 auto 0 62px}
.solution h3{font-family:var(--head);font-weight:600;font-size:12px;color:var(--charcoal);margin-top:22px;letter-spacing:.3px}
.solution p{font-size:9.5px;line-height:14px;color:#777;margin-top:5px;width:170px}
.solution .more{display:block;margin-top:10px;font-family:var(--head);font-size:9px;color:var(--orange);font-weight:500}
.solution-focus{position:absolute;left:481px;top:386px;width:241px;height:225px;background:var(--white);box-shadow:0 4px 18px rgba(0,0,0,.12)}

/* webinar */
.webinar{height:149px;background:var(--green)}
.webinar-head{position:absolute;left:279px;top:12px;font-family:var(--head);color:var(--white);white-space:nowrap;line-height:80px}
.webinar-head .light{font-weight:300;font-size:60px;letter-spacing:1px}
.webinar-head .bold{font-weight:700;font-size:80px;letter-spacing:2px;margin-left:16px}
.webinar-note{position:absolute;left:281px;top:98px;width:380px;font-size:9.5px;line-height:13px;color:#e6f1e1}

/* logo rows */
.media{height:307px}
.name-row{position:absolute;left:231px;width:738px;display:flex;justify-content:space-between;align-items:center}
.name-tile{font-family:var(--head);font-weight:600;color:var(--charcoal);display:flex;align-items:center;gap:6px;white-space:nowrap}
.name-tile .dot{width:12px;height:12px;background:#b5b5b5}

/* case studies */
.cases{height:665px;background:var(--light)}
.case-grid{position:absolute;left:231px;top:152px;width:738px;display:grid;grid-template-columns:repeat(3,238px);grid-auto-rows:218px;column-gap:12px;row-gap:13px}
.case{position:relative;overflow:hidden}
.case-media{position:absolute;inset:0}
.case-shade{position:absolute;inset:0;background:linear-gradient(180deg,rgba(0,0,0,0) 30%,rgba(0,0,0,.65) 100%)}
.case-body{position:absolute;left:12px;bottom:12px;width:170px;color:var(--white)}
.case-body h3{font-family:var(--head);font-weight:600;font-size:13px;letter-spacing:.4px}
.case-body p{font-size:9px;line-height:12px;margin:3px 0 9px}

/* clients */
.clients{height:307px}

/* achievements */
.achievements{height:342px;background:var(--green)}
.achievements .section-title{color:var(--white)}
.stat{position:absolute;width:130px;text-align:center;color:var(--white)}
.stat .label{font-size:12px;line-height:14px}
.stat .value{font-family:var(--head);font-weight:600;font-size:22px;line-height:28px}
.stat svg{display:block;margin:14px auto 0}

/* conferences */
.conferences{height:332px}
.conf-box{position:absolute;top:158px;height:111px;background:var(--light);display:flex;align-items:center;justify-content:center;gap:10px;font-family:var(--head);font-weight:600;font-size:26px;color:#4a4a4a;letter-spacing:1px}
.conf-box .mark{width:26px;height:26px;background:#4a4a4a}

/* blog */
.blog{height:507px;background:var(--light)}
.post{position:absolute;top:146px;width:238px;height:226px;background:var(--white)}
.post-media{height:133px}
.post-body{padding:10px 10px 0}
.post-body h3{font-family:var(--head);font-weight:600;font-size:11px;color:var(--link-blue);letter-spacing:.3px}
.post-body p{font-size:8.5px;line-height:12px;color:#777;margin-top:5px}
.post-meta{position:absolute;left:10px;right:10px;bottom:10px;display:flex;justify-content:space-between;font-size:7.5px;color:#666;text-transform:uppercase}
.post-meta b{color:var(--link-blue);font-weight:600}
.pager{position:absolute;top:428px;left:0;width:1200px;display:flex;justify-content:center;gap:7px}
.pager span{width:6px;height:6px;border-radius:50%;background:#cfcfcf}
.pager .on{background:var(--link-blue)}

/* about */
.about{height:500px}
.about-ghost{position:absolute;top:40px;width:1200px;text-align:center;font-family:var(--head);font-weight:700;font-size:130px;line-height:130px;color:#f1f1f1;letter-spacing:4px}
.about-media{position:absolute;left:231px;top:120px;width:386px;height:317px;box-shadow:0 6px 20px rgba(0,0,0,.2);background:linear-gradient(160deg,#8f8a86 0%,#5c5855 55%,#3e3b39 100%)}
.about-copy{position:absolute;left:655px;top:196px;width:314px}
.about-copy h2{font-family:var(--head);font-weight:600;font-size:22px;color:var(--charcoal);letter-spacing:.4px}
.about-copy p{font-size:9.5px;line-height:14px;color:#777;margin-top:12px}
.about-copy .btn{margin-top:14px}

/* footer */
.site-footer{height:386px;background:var(--footer);color:#cfcfcf}
.enquiry{position:absolute;top:26px;width:1200px;text-align:center}
.enquiry .label{font-family:var(--head);font-size:12px;color:var(--white);letter-spacing:1px;margin-top:4px}
.enquiry .phone{font-family:var(--head);font-weight:600;font-size:28px;color:var(--white);letter-spacing:1px;line-height:32px}
.footer-rule{position:absolute;left:231px;top:171px;width:738px;height:1px;background:#3a3a3a}
.footer-col{position:absolute;top:202px;font-size:8.5px;line-height:14px;color:#a8a8a8}
.footer-col h4{font-family:var(--head);font-weight:500;font-size:11px;color:var(--white);letter-spacing:.5px;margin-bottom:8px}
.footer-col li{list-style:none}
.copyright{position:absolute;left:231px;top:348px;font-size:8px;color:#8a8a8a}
.social{position:absolute;left:866px;top:344px;display:flex;gap:10px}
.social span{width:14px;height:14px;border-radius:50%;background:#4a4a4a}
</style>
</head>
<body>

<header class="hero">
  <div class="hero-media" role="img" aria-label="Photo of a smiling team member working in a bright open-plan office"></div>
  <div class="hero-shade"></div>
  <div class="brand"><span class="brand-mark"></span>BRIGHTLOOP</div>
  <nav class="main-nav">
    <span class="active">HOME</span><span>ABOUT</span><span>PPC</span><span>SEO</span><span>TRAINING</span><span>CLIENTS</span><span>STUDIES</span><span>BLOG</span><span>RESOURCES</span><span>CONTACT</span>
  </nav>
  <svg class="play" width="44" height="44" viewBox="0 0 44 44" aria-label="Play video">
    <circle cx="22" cy="22" r="21" fill="rgba(255,255,255,.35)"/>
    <path d="M17 13 L31 22 L17 31 Z" fill="#fff"/>
  </svg>
  <h1 class="hero-title">TIME IS LIMITED</h1>
  <p class="hero-sub">SO DON'T WASTE IT JOIN WITH US TO MAKE YOUR BUSINESS</p>
</header>

<section class="solutions">
  <h2 class="section-title" style="top:62px">Which box best describes your needs?</h2>
  <p class="section-intro" style="top:100px">Lorem Ipsum is simply dummy text of the printing and typesetting industry. Lorem Ipsum has been the industry's standard dummy text ever since the 1500s.</p>

  <div class="solution-focus"></div>

  <div class="solution" style="left:286px;top:185px">
    <svg width="36" height="36" viewBox="0 0 36 36" fill="none" stroke="#428E29" stroke-width="1.6"><path d="M5 17 L31 6 L24 30 L17 20 Z M17 20 L31 6"/></svg>
    <h3>LOREM IPSUM IS SIMPLY</h3>
    <p>Lorem Ipsum is simply dummy text of the printing and typesetting industry. Lorem Ipsum has been the industry's standard dummy.</p>
    <span class="more">READ MORE</span>
  </div>
  <div class="solution" style="left:533px;top:185px">
    <svg width="36" height="36" viewBox="0 0 36 36" fill="none" stroke="#428E29" stroke-width="1.6"><path d="M10 5 V31 M18 5 V31 M26 5 V31"/><rect x="7" y="10" width="6" height="4" fill="#fff"/><rect x="15" y="20" width="6" height="4" fill="#fff"/><rect x="23" y="13" width="6" height="4" fill="#fff"/></svg>
    <h3>LOREM IPSUM IS SIMPLY</h3>
    <p>Lorem Ipsum is simply dummy text of the printing and typesetting industry. Lorem Ipsum has been the industry's standard dummy.</p>
    <span class="more">READ MORE</span>
  </div>
  <div class="solution" style="left:780px;top:185px">
    <svg width="36" height="36" viewBox="0 0 36 36" fill="none" stroke="#428E29" stroke-width="1.6"><circle cx="18" cy="18" r="12"/><circle cx="18" cy="18" r="7"/><circle cx="18" cy="18" r="2"/><path d="M18 18 L30 6"/></svg>
    <h3>LOREM IPSUM IS SIMPLY</h3>
    <p>Lorem Ipsum is simply dummy text of the printing and typesetting industry. Lorem Ipsum has been the industry's standard dummy.</p>
    <span class="more">READ MORE</span>
  </div>

  <div class="solution" style="left:286px;top:418px">
    <svg width="36" height="36" viewBox="0 0 36 36" fill="none" stroke="#428E29" stroke-width="1.6"><circle cx="10" cy="18" r="3.5"/><circle cx="26" cy="9" r="3.5"/><circle cx="26" cy="27" r="3.5"/><path d="M13 16.5 L23 10.5 M13 19.5 L23 25.5"/></svg>
    <h3>LOREM IPSUM IS SIMPLY</h3>
    <p>Lorem Ipsum is simply dummy text of the printing and typesetting industry. Lorem Ipsum has been the industry's standard dummy.</p>
    <span class="more">READ MORE</span>
  </div>
  <div class="solution" style="left:533px;top:418px">
    <svg width="36" height="36" viewBox="0 0 36 36" fill="none" stroke="#428E29" stroke-width="1.6"><rect x="9" y="6" width="18" height="24" rx="1"/><path d="M13 12 H23 M13 17 H23 M13 22 H20"/></svg>
    <h3>LOREM IPSUM IS SIMPLY</h3>
    <p>Lorem Ipsum is simply dummy text of the printing and typesetting industry. Lorem Ipsum has been the industry's standard dummy.</p>
    <span class="more">READ MORE</span>
  </div>
  <div class="solution" style="left:780px;top:418px">
    <svg width="36" height="36" viewBox="0 0 36 36" fill="none" stroke="#428E29" stroke-width="1.6"><rect x="5" y="8" width="26" height="17" rx="1"/><path d="M14 30 H22 M18 25 V30 M10 20 L15 15 L19 18 L26 12"/></svg>
    <h3>LOREM IPSUM IS SIMPLY</h3>
    <p>Lorem Ipsum is simply dummy text of the printing and typesetting industry. Lorem Ipsum has been the industry's standard dummy.</p>
    <span class="more">READ MORE</span>
  </div>
</section>

<section class="webinar">
  <h2 class="webinar-head"><span class="light">FREE REGISTER</span><span class="bold">WEBINAR</span></h2>
  <p class="webinar-note">Lorem Ipsum is simply dummy text of the printing and typesetting industry. Lorem Ipsum has been the industry's standard dummy.</p>
</section>

<section class="media">
  <h2 class="section-title" style="top:62px">In the media</h2>
  <p class="section-intro" style="top:100px">Lorem Ipsum is simply dummy text of the printing and typesetting industry. Lorem Ipsum has been the industry's standard dummy text ever since the 1500s.</p>
  <div class="name-row" style="top:178px;height:50px">
    <span class="name-tile" style="font-size:18px">Harbourline</span>
    <span class="name-tile" style="font-size:18px">PLATEFUL</span>
    <span class="name-tile" style="font-size:13px">The Morning Courier</span>
    <span class="name-tile" style="font-size:17px">Ventura Weekly</span>
    <span class="name-tile" style="font-size:13px">The Coastal Herald</span>
    <span class="name-tile" style="font-size:13px"><span class="dot"></span>Ledger Review</span>
  </div>
</section>

<section class="cases">
  <h2 class="section-title" style="top:62px">Our case study</h2>
  <p class="section-intro" style="top:100px">Lorem Ipsum is simply dummy text of the printing and typesetting industry. Lorem Ipsum has been the industry's standard dummy text ever since the 1500s.</p>
  <div class="case-grid">
    <article class="case"><div class="case-media" role="img" aria-label="Photo of a team reviewing charts at a desk" style="background:linear-gradient(150deg,#a9a49c,#5d5a55)"></div><div class="case-shade"></div><div class="case-body"><h3>KORVA LEGAL</h3><p>Lorem Ipsum is simply dummy text of the printing and typesetting industry.</p><span class="btn">Read more</span></div></article>
    <article class="case"><div class="case-media" role="img" aria-label="Photo of hands working on a laptop and notes" style="background:linear-gradient(150deg,#b4aea5,#66615b)"></div><div class="case-shade"></div><div class="case-body"><h3>KORVA LEGAL</h3><p>Lorem Ipsum is simply dummy text of the printing and typesetting industry.</p><span class="btn">Read more</span></div></article>
    <article class="case"><div class="case-media" role="img" aria-label="Photo of a laptop showing analytics on a desk" style="background:linear-gradient(150deg,#c9c9c7,#6f7072)"></div><div class="case-shade"></div><div class="case-body"><h3>KORVA LEGAL</h3><p>Lorem Ipsum is simply dummy text of the printing and typesetting industry.</p><span class="btn">Read more</span></div></article>
    <article class="case"><div class="case-media" role="img" aria-label="Photo of a workspace with papers and a tablet" style="background:linear-gradient(150deg,#bdb7ad,#6a655e)"></div><div class="case-shade"></div><div class="case-body"><h3>KORVA LEGAL</h3><p>Lorem Ipsum is simply dummy text of the printing and typesetting industry.</p><span class="btn">Read more</span></div></article>
    <article class="case"><div class="case-media" role="img" aria-label="Photo of colleagues writing plans on paper" style="background:linear-gradient(150deg,#b0aaa1,#5f5b55)"></div><div class="case-shade"></div><div class="case-body"><h3>KORVA LEGAL</h3><p>Lorem Ipsum is simply dummy text of the printing and typesetting industry.</p><span class="btn">Read more</span></div></article>
    <article class="case"><div class="case-media" role="img" aria-label="Photo of a desk with a keyboard and coffee" style="background:linear-gradient(150deg,#9e9a94,#55524e)"></div><div class="case-shade"></div><div class="case-body"><h3>KORVA LEGAL</h3><p>Lorem Ipsum is simply dummy text of the printing and typesetting industry.</p><span class="btn">Read more</span></div></article>
  </div>
</section>

<section class="clients">
  <h2 class="section-title" style="top:62px">Our client</h2>
  <p class="section-intro" style="top:100px">Lorem Ipsum is simply dummy text of the printing and typesetting industry. Lorem Ipsum has been the industry's standard dummy text ever since the 1500s.</p>
  <div class="name-row" style="top:176px;height:50px">
    <span class="name-tile" style="font-size:20px;color:#8c8c8c"><span class="dot"></span>KVF</span>
    <span class="name-tile" style="font-size:12px;color:#8c8c8c">Keystone Proofing</span>
    <span class="name-tile" style="font-size:12px;color:#8c8c8c">Holbrook Storage</span>
    <span class="name-tile" style="font-size:13px;color:#8c8c8c">Snugfit</span>
    <span class="name-tile" style="font-size:15px;color:#8c8c8c">Ridgeway Tanks</span>
    <span class="name-tile" style="font-size:12px;color:#8c8c8c">Marlow Surveys</span>
  </div>
</section>

<section class="achievements">
  <h2 class="section-title" style="top:60px">Acheivements</h2>
  <div class="stat" style="left:223px;top:132px"><div class="label">Project</div><div class="value">20546</div>
    <svg width="34" height="34" viewBox="0 0 34 34" fill="none" stroke="#fff" stroke-width="1.4"><circle cx="17" cy="17" r="16"/><rect x="10" y="11" width="14" height="12"/><path d="M13 15 H21 M13 19 H19"/></svg></div>
  <div class="stat" style="left:372px;top:114px"><div class="label">Active Clients</div><div class="value">578</div>
    <svg width="34" height="34" viewBox="0 0 34 34" fill="none" stroke="#fff" stroke-width="1.4"><circle cx="17" cy="17" r="16"/><circle cx="17" cy="13" r="4"/><path d="M10 25 C10 19 24 19 24 25"/></svg></div>
  <div class="stat" style="left:530px;top:126px"><div class="label">Commitment</div><div class="value">250</div>
    <svg width="34" height="34" viewBox="0 0 34 34" fill="none" stroke="#fff" stroke-width="1.4"><circle cx="17" cy="17" r="16"/><path d="M9 19 L14 14 L19 18 L25 12 M21 12 H25 V16"/></svg></div>
  <div class="stat" style="left:679px;top:158px"><div class="label">Success Rate</div><div class="value">96</div>
    <svg width="34" height="34" viewBox="0 0 34 34" fill="none" stroke="#fff" stroke-width="1.4"><circle cx="17" cy="17" r="16"/><path d="M11 17 L15 21 L23 13"/></svg></div>
  <div class="stat" style="left:834px;top:158px"><div class="label">Unethical Parctice</div><div class="value">05</div>
    <svg width="34" height="34" viewBox="0 0 34 34" fill="none" stroke="#fff" stroke-width="1.4"><circle cx="17" cy="17" r="16"/><path d="M17 9 V25 M11 25 H23 M10 12 H24 M10 12 L7 19 H13 Z M24 12 L21 19 H27 Z"/></svg></div>
  <svg class="abs" style="left:0;top:244px" width="1200" height="98" viewBox="0 0 1200 98" preserveAspectRatio="none">
    <path d="M0 50 C120 10 220 30 330 45 C450 62 520 20 640 28 C760 36 820 60 930 40 C1040 20 1120 30 1200 44 V98 H0 Z" fill="#3a8224"/>
    <path d="M0 72 C160 52 260 78 420 64 C560 52 660 80 800 70 C940 60 1060 76 1200 66 V98 H0 Z" fill="#2f7420"/>
  </svg>
</section>

<section class="conferences">
  <h2 class="section-title" style="top:58px">Conference</h2>
  <p class="section-intro" style="top:94px">Lorem Ipsum is simply dummy text of the printing and typesetting industry. Lorem Ipsum has been the industry's standard dummy text ever since the 1500s.</p>
  <div class="conf-box" style="left:231px;width:234px"><span class="mark"></span>STACKCON</div>
  <div class="conf-box" style="left:491px;width:228px;font-size:18px">TIDEMEET LOCAL</div>
  <div class="conf-box" style="left:738px;width:231px;font-size:22px"><span class="mark"></span>QRX SUMMIT</div>
</section>

<section class="blog">
  <h2 class="section-title" style="top:56px">Latest blog</h2>
  <p class="section-intro" style="top:96px">Lorem Ipsum is simply dummy text of the printing and typesetting industry. Lorem Ipsum has been the industry's standard dummy text ever since the 1500s.</p>
  <article class="post" style="left:231px"><div class="post-media" role="img" aria-label="Photo of a team meeting around a table" style="background:linear-gradient(150deg,#6c7078,#34373c)"></div><div class="post-body"><h3>LOREM IPSUM IS SIMPLY DUMMY</h3><p>Lorem Ipsum is simply dummy text of the printing and typesetting industry. Lorem Ipsum has been the industry's standard.</p></div><div class="post-meta"><span>Pallwall | <b>Blipster</b> | Zentro Hub</span><span>Read more</span></div></article>
  <article class="post" style="left:481px"><div class="post-media" role="img" aria-label="Photo of people talking in a cafe workspace" style="background:linear-gradient(150deg,#7a6f64,#3a332d)"></div><div class="post-body"><h3>LOREM IPSUM IS SIMPLY DUMMY</h3><p>Lorem Ipsum is simply dummy text of the printing and typesetting industry. Lorem Ipsum has been the industry's standard.</p></div><div class="post-meta"><span>Pallwall | <b>Blipster</b> | Zentro Hub</span><span>Read more</span></div></article>
  <article class="post" style="left:731px"><div class="post-media" role="img" aria-label="Photo of a speaker at a conference stage" style="background:linear-gradient(150deg,#6a6f7a,#2f333a)"></div><div class="post-body"><h3>LOREM IPSUM IS SIMPLY DUMMY</h3><p>Lorem Ipsum is simply dummy text of the printing and typesetting industry. Lorem Ipsum has been the industry's standard.</p></div><div class="post-meta"><span>Pallwall | <b>Blipster</b> | Zentro Hub</span><span>Read more</span></div></article>
  <div class="pager"><span></span><span></span><span></span><span class="on"></span><span></span></div>
</section>

<section class="about">
  <div class="about-ghost" aria-hidden="true">ABOUT US</div>
  <div class="about-media" role="img" aria-label="Group photo of the agency team standing together"></div>
  <div class="about-copy">
    <h2>INTEREST IN WORKING WITH US?</h2>
    <p>Lorem Ipsum is simply dummy text of the printing and typesetting industry. Lorem Ipsum has been the industry's standard dummy text ever since the 1500s, when an unknown printer took a galley of type and scrambled it to make a type specimen book.</p>
    <p>Lorem Ipsum is simply dummy text of the printing and typesetting industry. Lorem Ipsum has been the industry's standard dummy text ever since the 1500s, when an unknown printer took a galley of type and scrambled it to make a type specimen book.</p>
    <span class="btn">Read more</span>
  </div>
</section>

<footer class="site-footer">
  <div class="enquiry">
    <svg width="46" height="46" viewBox="0 0 46 46" fill="none" stroke="#de7532" stroke-width="2"><path d="M40 23 A17 17 0 1 1 34 10"/><path d="M34 4 V10 H28"/><text x="23" y="28" text-anchor="middle" font-family="Oswald, sans-serif" font-size="14" font-weight="600" fill="#de7532" stroke="none">24</text></svg>
    <div class="label">ANY ENQUIRY</div>
    <div class="phone">1300 555 017</div>
  </div>
  <div class="footer-rule"></div>
  <div class="footer-col" style="left:231px;width:170px">
    <h4>GET IN TOUCH</h4>
    <ul><li>Level 4, 18 Larkin Street</li><li>Harbourside Business Park,</li><li>Sydney, NSW 2000</li><li style="margin-top:8px">(02) 5550 1740</li><li style="margin-top:8px">hello@brightloop.example</li></ul>
  </div>
  <div class="footer-col" style="left:434px">
    <h4>INFORMATION</h4>
    <ul><li>Home</li><li>About</li><li>PPC</li><li>SEO</li><li>Training</li></ul>
  </div>
  <div class="footer-col" style="left:526px;padding-top:22px">
    <ul><li>Client</li><li>Success</li><li>Blog</li><li>Resources</li><li>Contact</li></ul>
  </div>
  <div class="footer-col" style="left:655px">
    <h4>SEO</h4>
    <ul><li>SEO Management</li><li>SEO Audits</li><li>SEO Consulting</li><li>Analytics Services</li></ul>
  </div>
  <div class="footer-col" style="left:830px">
    <h4>RESOURCES</h4>
    <ul><li>Podcasts</li><li>eBooks</li><li>Our Blog</li></ul>
  </div>
  <p class="copyright">Copyright © 2018 BrightLoop</p>
  <div class="social" aria-label="Social links: Pallwall, Blipster, Zentro Hub, ReelDrop, WorkMesh"><span></span><span></span><span></span><span></span><span></span></div>
</footer>

</body>
</html>
```